Book cover for book about Climate Change

Looking for a clean, bold, and attractive cover for a mass-market paperback (5.5"x 8.5") about solving the climate change problem. Title is either "When Rivers Learn to Sing” or A Lantern Over Quiet Fields” (your choice), subtitle is "A five-step plan to reverse climate change — to ensure that your grandchildren will live on a clean and comfortable planet," author is Dale Pruitt. Thinking that it *might* feature an image of Earth (or a portion thereof) and its very thin layer of atmosphere -- but STRONGLY encourage other ideas too!

Requirements
Nice to have
• Keep it positive — NOT scary doom-and-gloom

```html
<!DOCTYPE html>
<html lang="en">
<head>
<meta charset="utf-8">
<title>When Rivers Learn to Sing — Dale Pruitt</title>
<link href="https://fonts.googleapis.com/css2?family=Montserrat:wght@300&family=Open+Sans:wght@400;600;800&family=Allura&display=swap" rel="stylesheet">
<style>
  :root {
    --night-top: #1b2d4a;
    --night-mid: #0b1527;
    --night-bottom: #060a12;
    --glow: rgba(44,111,192,0.45);
    --earth-light: #a9cdee;
    --earth-mid: #3a78b8;
    --earth-dark: #0b1f3c;
    --rim: rgba(110,175,245,0.55);
    --skin: rgba(214,170,148,0.55);
    --ink: #ffffff;
    --rule: rgba(255,255,255,0.5);
  }
  html, body {
    margin: 0;
    padding: 0;
    width: 840px;
    height: 1200px;
    overflow: hidden;
    background: var(--night-bottom);
  }
  .cover {
    position: relative;
    width: 840px;
    height: 1200px;
    overflow: hidden;
    background:
      radial-gradient(ellipse 420px 150px at 50% 870px, var(--glow), transparent 72%),
      linear-gradient(180deg, var(--night-top) 0%, var(--night-mid) 45%, var(--night-bottom) 100%);
  }
  .hero-photo {
    position: absolute;
    left: 0;
    top: 0;
    width: 840px;
    height: 620px;
    background:
      radial-gradient(circle 262px at 450px 328px, var(--earth-light) 0%, var(--earth-mid) 30%, var(--earth-dark) 78%, rgba(11,31,60,0.6) 96%, transparent 100%),
      radial-gradient(circle 285px at 450px 328px, var(--rim) 0%, transparent 100%),
      radial-gradient(ellipse 130px 280px at 20px 260px, var(--skin), transparent 100%),
      radial-gradient(ellipse 130px 280px at 820px 260px, var(--skin), transparent 100%);
  }
  .author {
    position: absolute;
    top: 34px;
    left: 0;
    width: 100%;
    margin: 0;
    text-align: center;
    font-family: "Montserrat", sans-serif;
    font-weight: 300;
    font-size: 40px;
    line-height: 48px;
    letter-spacing: 9px;
    color: var(--ink);
  }
  .title {
    position: absolute;
    top: 612px;
    left: 0;
    width: 100%;
    margin: 0;
    text-align: center;
    color: var(--ink);
  }
  .title__lead {
    display: block;
    font-family: "Open Sans", sans-serif;
    font-weight: 600;
    font-size: 68px;
    line-height: 88px;
  }
  .title__joiner {
    display: flex;
    align-items: center;
    justify-content: center;
    gap: 24px;
    height: 64px;
    margin-top: 2px;
  }
  .title__rule {
    width: 246px;
    height: 1px;
    background: var(--rule);
  }
  .title__script {
    font-family: "Allura", cursive;
    font-weight: 400;
    font-size: 78px;
    line-height: 64px;
    padding: 0 6px;
  }
  .title__main {
    display: block;
    font-family: "Open Sans", sans-serif;
    font-weight: 800;
    font-size: 214px;
    line-height: 190px;
    letter-spacing: -4px;
    margin-top: -4px;
  }
  .subtitle {
    position: absolute;
    top: 1006px;
    left: 30px;
    width: 780px;
    margin: 0;
    text-align: center;
    font-family: "Open Sans", sans-serif;
    font-weight: 400;
    font-size: 20.5px;
    line-height: 28px;
    color: var(--ink);
    text-transform: uppercase;
  }
</style>
</head>
<body>
  <main class="cover">
    <div class="hero-photo" role="img" aria-label="Photograph of two cupped hands gently sheltering planet Earth with its glowing blue atmosphere"></div>

    <p class="author">DALE PRUITT</p>

    <h1 class="title">
      <span class="title__lead">WHEN RIVERS LEARN</span>
      <span class="title__joiner">
        <span class="title__rule"></span>
        <span class="title__script">to</span>
        <span class="title__rule"></span>
      </span>
      <span class="title__main">SING</span>
    </h1>

    <p class="subtitle">A five-step plan to reverse climate change - to ensure that your<br>grandchildren will live on a clean and comfortable planet</p>
  </main>
</body>
</html>
```